Facebook Header Design Project.

I'm supplying white and colored logos. The Facebook page already exists. URL = https://www.pagebook.example/lumocrest.design The design should not be based on what's already there. Consider mobile implications of the design. This Design will form the designs of other social media headers. LumoCrest is a web design | digital marketing company.

Target Market(s)

People interested in web design | digital marketing services.

Industry/Entity Type

LumoCrest is a web design | digital marketing company. That should be clear in the design.

Colors
0054AA
0677BA
7BADD7
CADEEF
E8F1F8

Requirements
Must have
• Logo. Use Facebook header image dimension.
Nice to have
• Use a color scheme like the logo and feel free to add a color or two from the other side of the color whee.

```html
<!DOCTYPE html>
<html lang="en">
<head>
<meta charset="utf-8">
<title>LumoCrest – Digital Marketing Header</title>
<link rel="stylesheet" href="https://fonts.googleapis.com/css2?family=Saira+Condensed:wght@700;800&family=Mulish:wght@400;600;700;800&display=swap">
<style>
  :root {
    --navy: #0054AA;
    --blue: #0677BA;
    --sky: #7BADD7;
    --mist: #CADEEF;
    --frost: #E8F1F8;
    --stone: #F3F2F0;
    --ink: #2B2B2B;
    --rule: #1E3A6B;
    --page: #EDEDED;
    --white: #FFFFFF;
  }
  * { margin: 0; padding: 0; box-sizing: border-box; }
  html, body { width: 1200px; height: 643px; overflow: hidden; }
  body { background: var(--page); font-family: "Mulish", sans-serif; color: var(--ink); position: relative; }

  .header-banner {
    position: absolute; left: 20px; top: 89px;
    width: 1160px; height: 465px;
    background: var(--white); overflow: hidden;
  }
  .banner-art { position: absolute; inset: 0; width: 1160px; height: 465px; }

  .brand {
    position: absolute; left: 64px; top: 50px;
    display: flex; align-items: center; gap: 6px;
    font-weight: 800; font-size: 15px; color: var(--navy);
  }
  .brand-mark { width: 12px; height: 12px; background: var(--navy); }

  .eyebrow {
    position: absolute; left: 64px; top: 160px;
    font-family: "Saira Condensed", sans-serif; font-weight: 800;
    font-size: 21px; line-height: 1; color: #1F1F1F; letter-spacing: 0.2px;
  }
  .headline {
    position: absolute; left: 64px; top: 180px;
    font-family: "Saira Condensed", sans-serif; font-weight: 800;
    font-size: 56px; line-height: 1; color: var(--blue); letter-spacing: 0.3px;
    white-space: nowrap;
  }
  .headline-rule {
    position: absolute; left: 64px; top: 238px;
    width: 142px; height: 2px; background: var(--rule);
  }
  .intro {
    position: absolute; left: 64px; top: 246px; width: 320px;
    font-size: 12.6px; line-height: 17.6px; font-weight: 600; color: #333;
  }

  .contact-pill {
    position: absolute; left: 64px; top: 332px;
    width: 293px; height: 34px; border-radius: 17px;
    background: var(--blue); display: flex; align-items: center;
  }
  .contact-label {
    height: 34px; width: 126px; border-radius: 17px;
    background: var(--navy); color: var(--white);
    font-size: 11px; font-weight: 800; letter-spacing: 0.3px;
    display: flex; align-items: center; padding-left: 26px;
  }
  .contact-phone {
    flex: 1; text-align: center; color: var(--white);
    font-size: 14.5px; font-weight: 800; padding-left: 4px;
  }
  .page-link {
    position: absolute; left: 381px; top: 340px;
    font-size: 13px; font-weight: 700; color: #333;
  }

  .service-list {
    position: absolute; left: 0; top: 408px; height: 24px;
    list-style: none;
  }
  .service-list li {
    position: absolute; top: 0; white-space: nowrap;
    font-size: 16px; font-weight: 600; color: #333; line-height: 24px;
    padding-left: 14px;
  }
  .service-list li::before {
    content: ""; position: absolute; left: 0; top: 8.5px;
    width: 8px; height: 8px; border-radius: 50%; background: var(--blue);
  }
  .service-graphic { left: 68px; }
  .service-web { left: 223px; }
  .service-marketing { left: 356px; }
  .service-dev { left: 520px; }
</style>
</head>
<body>
  <section class="header-banner">
    <svg class="banner-art" viewBox="0 0 1160 465" xmlns="http://www.w3.org/2000/svg">
      <defs>
        <linearGradient id="stripe-fade" x1="0" y1="0" x2="0" y2="1">
          <stop offset="0" stop-color="#1E3A6B"/>
          <stop offset="1" stop-color="#0677BA"/>
        </linearGradient>
        <linearGradient id="office-warm" x1="0" y1="0" x2="1" y2="1">
          <stop offset="0" stop-color="#D9D2C8"/>
          <stop offset="1" stop-color="#5A4A42"/>
        </linearGradient>
        <linearGradient id="meeting-room" x1="0" y1="0" x2="1" y2="1">
          <stop offset="0" stop-color="#8A6B52"/>
          <stop offset="1" stop-color="#D8C7B4"/>
        </linearGradient>
        <linearGradient id="desk-work" x1="0" y1="0" x2="1" y2="1">
          <stop offset="0" stop-color="#7C7470"/>
          <stop offset="1" stop-color="#B9C9CC"/>
        </linearGradient>
        <linearGradient id="bright-office" x1="0" y1="0" x2="1" y2="1">
          <stop offset="0" stop-color="#F2F4F5"/>
          <stop offset="1" stop-color="#D5D9DC"/>
        </linearGradient>
      </defs>
      <rect class="band-frost" x="0" y="115" width="720" height="185" fill="#E8F1F8"/>
      <rect class="band-stone" x="0" y="387" width="760" height="67" fill="#F3F2F0"/>
      <polygon class="accent-stripe" points="318,0 334,0 772,465 722,465" fill="url(#stripe-fade)"/>
      <polygon role="img" aria-label="Photo of a presenter handing out cards in a team office" points="326,0 633,0 842,231 534,231" fill="url(#office-warm)"/>
      <polygon role="img" aria-label="Photo of a team meeting around a conference table with laptops" points="647,0 1160,0 1160,231 855,231" fill="url(#meeting-room)"/>
      <polygon role="img" aria-label="Photo of hands sketching plans beside laptops on a desk" points="538,235 878,235 1069,465 746,465" fill="url(#desk-work)"/>
      <polygon role="img" aria-label="Photo of two colleagues in a bright office by the windows" points="888,235 1160,235 1160,465 1080,465" fill="url(#bright-office)"/>
    </svg>

    <div class="brand"><span class="brand-mark"></span>LumoCrest</div>

    <p class="eyebrow">LUMOCREST</p>
    <h1 class="headline">DIGITAL MARKETING</h1>
    <div class="headline-rule"></div>
    <p class="intro">LumoCrest provides web design and development, SEO, and graphic design services.</p>

    <div class="contact-pill">
      <span class="contact-label">CONTACT US</span>
      <span class="contact-phone">+1 555-014-2087</span>
    </div>
    <p class="page-link">pagebook.example/lumocrest.design</p>

    <ul class="service-list">
      <li class="service-graphic">Graphic Design</li>
      <li class="service-web">Web Design</li>
      <li class="service-marketing">Digital Marketing</li>
      <li class="service-dev">Development</li>
    </ul>
  </section>
</body>
</html>
```